a mobile app for beauty salon professional to publish their service and customers to book service

I plan to create an iPhone app (support iPhone 6 and above) that will allow beauty salon professionals (e.g. hair stylist) to publish their service/business with address/geolocation and available time slots, manage their professional profile with photos, and service charges, allow the customers to search services based on locations, and book the service. customer can provide feedback/ratings on the professional's service. a reference website : http://mira.tovelpa.example/booking/

Target Market(s)

beauty and hair salon professionals and customers

Industry/Entity Type

Hair And Beauty

Font styles to use
Sans Serif
Script

Colors

Designer to choose colors to be used in the design.

Requirements
Must have
• === customer features
• - user/customer registration
• - customer browse nearby service using a map view
• - customer browse nearby service using a list view ordered by distance (e.g. km)
• - customer search salon service based on service category, price range, and profressional's rating
• - customer select a service with zoom in details : salon name, service offered, location/address, and a "booking" button
• - customer place booking by specifying service (e.g. simple cut, blow-dry, etc) required, time slot, preferred professional
• - customer payments (paypal/credit card)
• - customer can feedback/rate on the salon professional
• === salon professional features
• - user/professional registration
• - maintain professional profile (private/public), option to upload photos
• - a registered professional can register/maintain shop/business who by default is the owner of the shop/business
• - a shop owner can assign professionals to the shop/business (multiple professional can work in the same location/shop)
• - professional maintain their service and schedule (breaks, holidays, working hours, appointments, service rates)

```html
<!DOCTYPE html>
<html lang="en">
<head>
<meta charset="utf-8">
<title>Velvo – Salon Finder Home</title>
<link href="https://fonts.googleapis.com/css2?family=Abril+Fatface&family=Open+Sans:wght@400;600&family=Poppins:wght@800&display=swap" rel="stylesheet">
<style>
  :root {
    --backdrop: #3b3b3b;
    --paper: #ffffff;
    --ink: #111111;
    --night: #050505;
    --stripe: #141414;
    --sky: #0aa9da;
    --leaf: #0fc73a;
    --leaf-deep: #0a7f24;
    --magenta: #d4128f;
    --card: rgba(196, 196, 196, 0.78);
    --card-text: #111111;
    --card-sub: #ffffff;
    --go: #2f7fbd;
    --go-teal: #117ea0;
    --heart: #19e43a;
  }
  * { box-sizing: border-box; margin: 0; padding: 0; }
  html, body { width: 778px; height: 1200px; overflow: hidden; background: var(--backdrop); }
  .canvas { position: relative; width: 778px; height: 1200px; overflow: hidden; }
  .screen { position: absolute; left: 51px; top: 0; width: 675px; height: 1200px; overflow: hidden; background: var(--night); font-family: "Open Sans", sans-serif; }

  .header { position: absolute; inset: 0 0 auto 0; height: 227px; background: var(--paper); z-index: 5; }
  .status { position: absolute; top: 6px; left: 14px; right: 12px; height: 26px; display: flex; align-items: center; justify-content: space-between; font-size: 20px; color: var(--ink); }
  .status-time { position: absolute; left: 50%; transform: translateX(-50%); font-weight: 600; }
  .status-left, .status-right { display: flex; align-items: center; gap: 6px; }
  .brand { position: absolute; left: 37px; top: 38px; font-family: "Abril Fatface", serif; font-size: 46px; letter-spacing: 1px; color: var(--ink); }
  .menu { position: absolute; left: 575px; top: 53px; width: 57px; height: 33px; }
  .search { position: absolute; left: 30px; top: 124px; width: 506px; height: 69px; border: 2px solid var(--ink); border-radius: 35px; display: flex; align-items: center; padding: 0 28px 0 30px; justify-content: space-between; font-size: 32px; color: var(--ink); }
  .filter { position: absolute; left: 562px; top: 124px; width: 70px; height: 70px; border: 2px solid var(--ink); border-radius: 50%; display: flex; align-items: center; justify-content: center; }

  .stage { position: absolute; left: 0; top: 227px; width: 675px; height: 973px; }
  .stage svg.decor { position: absolute; inset: 0; }
  .portrait { position: absolute; left: 280px; top: 0; width: 395px; height: 973px;
    background: radial-gradient(ellipse 60% 55% at 70% 48%, rgba(212,18,143,0.95), rgba(150,10,100,0.7) 55%, rgba(0,0,0,0) 100%); }

  .discover { position: absolute; left: 69px; top: 303px; width: 536px; height: 92px; border-radius: 46px; background: var(--sky); display: flex; align-items: center; justify-content: center; gap: 18px; font-family: "Poppins", sans-serif; font-weight: 800; font-size: 37px; color: var(--paper); z-index: 3; }

  .tab { position: absolute; font-family: "Abril Fatface", serif; font-size: 42px; color: var(--paper); z-index: 3; }
  .tab-booked { left: 76px; top: 552px; }
  .tab-seen { left: 80px; top: 612px; }
  .tab-rule { position: absolute; left: 71px; top: 607px; width: 525px; height: 2px; background: var(--paper); z-index: 3; }
  .chev { position: absolute; left: 576px; width: 36px; height: 22px; z-index: 3; }

  .salon { position: absolute; left: 66px; width: 539px; height: 112px; border-radius: 14px; overflow: hidden; background: var(--card); z-index: 3; }
  .salon-info { position: absolute; left: 33px; top: 12px; }
  .salon-name { font-size: 25px; font-weight: 600; color: var(--card-text); line-height: 32px; }
  .salon-line { font-size: 18.5px; color: var(--card-sub); line-height: 26px; }
  .salon-rating { position: absolute; left: 318px; top: 20px; display: flex; gap: 4px; align-items: center; }
  .salon-go { position: absolute; right: 0; top: 0; width: 69px; height: 112px; background: var(--go); display: flex; align-items: center; justify-content: center; }
  .salon-go.teal { background: var(--go-teal); }
</style>
</head>
<body>
<div class="canvas">
  <div class="screen">
    <header class="header">
      <div class="status">
        <div class="status-left">
          <svg width="62" height="14" viewBox="0 0 62 14"><circle cx="7" cy="7" r="5.5" fill="#111"/><circle cx="20" cy="7" r="5.5" fill="#111"/><circle cx="33" cy="7" r="5.5" fill="#111"/><circle cx="46" cy="7" r="5" fill="none" stroke="#111" stroke-width="1.3"/><circle cx="58" cy="7" r="3.5" fill="none" stroke="#111" stroke-width="1.3"/></svg>
          <span>NOVA</span>
          <svg width="22" height="16" viewBox="0 0 22 16"><path d="M2 6a13 13 0 0 1 18 0M5 9a9 9 0 0 1 12 0M8 12a4.5 4.5 0 0 1 6 0" fill="none" stroke="#111" stroke-width="2.2" stroke-linecap="round"/></svg>
        </div>
        <span class="status-time">4:21 PM</span>
        <div class="status-right">
          <svg width="12" height="20" viewBox="0 0 12 20"><path d="M1 5l10 9-5 4V2l5 4-10 9" fill="none" stroke="#777" stroke-width="1.4"/></svg>
          <span>100%</span>
          <svg width="44" height="18" viewBox="0 0 44 18"><rect x="1" y="1" width="38" height="16" rx="3" fill="none" stroke="#111" stroke-width="1.5"/><rect x="3" y="3" width="34" height="12" rx="1.5" fill="#111"/><rect x="40.5" y="6" width="2.5" height="6" fill="#111"/></svg>
        </div>
      </div>
      <div class="brand">Velvo</div>
      <svg class="menu" viewBox="0 0 57 33"><rect x="0" y="0" width="50" height="5" rx="2.5" fill="#111"/><rect x="0" y="14" width="57" height="5" rx="2.5" fill="#111"/><rect x="0" y="28" width="57" height="5" rx="2.5" fill="#111"/></svg>
      <div class="search">
        <span>Quick Search</span>
        <svg width="34" height="34" viewBox="0 0 34 34"><circle cx="20" cy="14" r="11" fill="none" stroke="#111" stroke-width="2.4"/><path d="M12 22L3 31" stroke="#111" stroke-width="2.6" stroke-linecap="round"/></svg>
      </div>
      <div class="filter">
        <svg width="30" height="30" viewBox="0 0 30 30"><path d="M2 4h26L18 15v11l-6-3v-8z" fill="#111"/></svg>
      </div>
    </header>

    <section class="stage">
      <svg class="decor" width="675" height="973" viewBox="0 0 675 973">
        <defs>
          <radialGradient id="leafGlow" cx="0.5" cy="0.35" r="0.6">
            <stop offset="0" stop-color="#12d441"/>
            <stop offset="0.7" stop-color="#0a9a2b"/>
            <stop offset="1" stop-color="#053d11" stop-opacity="0.2"/>
          </radialGradient>
        </defs>
        <path d="M0 260L300 0H420L0 370Z" fill="var(--stripe)"/>
        <path d="M0 720L380 400H470L0 820Z" fill="var(--stripe)"/>
        <circle cx="164" cy="280" r="134" fill="url(#leafGlow)"/>
        <circle cx="601" cy="45" r="45" fill="url(#leafGlow)"/>
        <circle cx="136" cy="851" r="78" fill="url(#leafGlow)"/>
      </svg>
      <div class="portrait" role="img" aria-label="Magenta-toned photo of a woman with long hair, head tilted back"></div>
    </section>

    <div class="discover">
      <span>Discover Nearby</span>
      <svg width="48" height="50" viewBox="0 0 48 50"><path d="M24 38C14 26 11 20 11 15a13 13 0 0 1 26 0c0 5-3 11-13 23z" fill="none" stroke="#fff" stroke-width="2"/><circle cx="24" cy="15" r="5" fill="none" stroke="#fff" stroke-width="2"/><path d="M16 34C7 35 2 38 2 41c0 4 10 7 22 7s22-3 22-7c0-3-5-6-14-7" fill="none" stroke="#fff" stroke-width="2"/></svg>
    </div>

    <div class="tab tab-booked">Booked</div>
    <svg class="chev" style="top:583px" viewBox="0 0 36 22"><path d="M3 4l15 14L33 4" fill="none" stroke="#fff" stroke-width="3.5"/></svg>
    <div class="tab-rule"></div>
    <div class="tab tab-seen">Last seen</div>
    <svg class="chev" style="top:643px" viewBox="0 0 36 22"><path d="M3 4l15 14L33 4" fill="none" stroke="var(--heart)" stroke-width="3.5"/></svg>

    <article class="salon" style="top:687px">
      <div class="salon-info">
        <div class="salon-name">Lumea Hair Studio</div>
        <div class="salon-line">Stylist Clara Voss</div>
        <div class="salon-line">8 Cedarbrook, Stone Ridge</div>
      </div>
      <div class="salon-rating">
        <svg width="108" height="20" viewBox="0 0 108 20"><g fill="#fff"><path id="st" d="M10 1l2.6 6 6.4.5-4.9 4.2 1.5 6.3L10 14.6 4.4 18l1.5-6.3L1 7.5 7.4 7z"/><use href="#st" x="22"/><use href="#st" x="44"/><use href="#st" x="66"/><use href="#st" x="88"/></g></svg>
        <svg width="24" height="22" viewBox="0 0 24 22"><path d="M12 21C4 14 1 10 1 6a5.5 5.5 0 0 1 11-1 5.5 5.5 0 0 1 11 1c0 4-3 8-11 15z" fill="var(--heart)"/></svg>
      </div>
      <div class="salon-go"><svg width="22" height="36" viewBox="0 0 22 36"><path d="M3 3l15 15L3 33" fill="none" stroke="#fff" stroke-width="3"/></svg></div>
    </article>

    <article class="salon" style="top:817px">
      <div class="salon-info">
        <div class="salon-name">Rosewind</div>
        <div class="salon-line">Stylist Milo R Hartley</div>
        <div class="salon-line">2241 Larkspur Lane,Ohio</div>
      </div>
      <div class="salon-rating">
        <svg width="108" height="20" viewBox="0 0 108 20"><g fill="#fff"><use href="#st"/><use href="#st" x="22"/><use href="#st" x="44"/><use href="#st" x="66"/><use href="#st" x="88"/></g></svg>
        <svg width="24" height="22" viewBox="0 0 24 22"><path d="M12 21C4 14 1 10 1 6a5.5 5.5 0 0 1 11-1 5.5 5.5 0 0 1 11 1c0 4-3 8-11 15z" fill="var(--heart)"/></svg>
      </div>
      <div class="salon-go"><svg width="22" height="36" viewBox="0 0 22 36"><path d="M3 3l15 15L3 33" fill="none" stroke="#fff" stroke-width="3"/></svg></div>
    </article>

    <article class="salon" style="top:946px">
      <div class="salon-info">
        <div class="salon-name">Coral Breeze</div>
        <div class="salon-line">Stylist Owen T Brandt</div>
        <div class="salon-line">590 Elm Avenue,Dalton</div>
      </div>
      <div class="salon-rating">
        <svg width="108" height="20" viewBox="0 0 108 20"><g fill="#fff"><use href="#st"/><use href="#st" x="22"/><use href="#st" x="44"/><use href="#st" x="66"/><use href="#st" x="88"/></g></svg>
      </div>
      <div class="salon-go teal"><svg width="22" height="36" viewBox="0 0 22 36"><path d="M3 3l15 15L3 33" fill="none" stroke="#fff" stroke-width="3"/></svg></div>
    </article>
  </div>
</div>
</body>
</html>
```